Pool Website

Need a simple front page and one internal page for a pool construction website. Please read the Must Have section for info. We uploaded 2 logos, one with color and one black and white. The colors you use in the logo can be changed, we used Century Gothic for the typing under the logo.

Nice clean design. The main back behind the site can be any color but we want the content back ground to be white.

We want a scrolling photo gallery (it doesn't have to scroll in your sample just know that's what we are envisioning) on the front page and the menu, and maybe a couple of photos down below to be clicked on such as this http://www.dellmorepools.example/

The 2ndary page would still have a header and menu and some type of cool design. Could be similar to this http://www.dellmorepools.example/about-us/awards.html

Also some other designs they like are here http://www.trelvacraft.example/14-examples-of-clean-modern-website-design-inspiration/ I realize not all of these could have a image scroller on the front page which is fine.

Please do not copy their site exactly though it must be different.

For now you can just use sample stock photography for your photos for the design but ultimately we will swap them out for our own photos so there will not be a need to purchase stock photography of pools.

Menus will include Home - About - Services - Gallery - Contact - Blog

The current site is http://www.gilesfentonpools.example/ we do not want it to look anything like this. It's way too dark and just not professional looking. We want this new site to look very slick and professional.

We also want a space for social networking logos etc.

I have also attached 2 zip files that contain photos that may be used in the design. You do not have to use them all but you are welcome to use a few. Most will be put in the photo gallery.

Colors: Blues, white, grays, black, etc.
Updates

Added several photos that can be used in the design. Obviously you do not have to use them all most will be in the photo gallery but you're welcome to use some for your design. 

Target Market(s)

People with money for residential pools or companies that want corporate pools. Are target location is Miami and California

Industry/Entity Type

Construction

Font styles to use
Serif
Sans Serif

Requirements
Must have
• Nice clean design. The main back behind the site can be any color but we want the content back ground to be white.

```html
<!DOCTYPE html>
<html lang="en">
<head>
<meta charset="utf-8">
<title>Giles Fenton Pools</title>
<link href="https://fonts.googleapis.com/css2?family=Open+Sans:wght@300;400;600;700&display=swap" rel="stylesheet">
<style>
:root{
  --navy:#1d2a7a;
  --teal:#1fb5c4;
  --ink:#111;
  --body:#444;
  --rule:#e6e8ee;
  --footer:#555;
  --footer-base:#2e2e2e;
  --white:#fff;
}
*{margin:0;padding:0;box-sizing:border-box}
html,body{width:1200px;height:1172px;overflow:hidden;background:var(--white);font-family:"Open Sans",Arial,sans-serif;color:var(--ink)}
.page{position:relative;width:1200px;height:1172px}
.top-strip{position:absolute;left:0;top:0;width:1200px;height:4px;background:#000}
.site-header{position:absolute;left:0;top:4px;width:1200px;height:110px;border-bottom:1px solid var(--rule)}
.brand{position:absolute;left:187px;top:20px;display:flex;align-items:center;gap:8px}
.brand-mark{width:22px;height:22px;background:var(--navy)}
.brand-name{font-size:15px;font-weight:700;color:var(--navy)}
.main-nav{position:absolute;left:455px;top:43px;display:flex;font-size:9px;text-transform:uppercase}
.main-nav a{display:block;height:23px;line-height:23px;color:var(--ink);text-decoration:none;text-align:center}
.main-nav a.current{background:#000;color:var(--white);width:87px;text-transform:none;font-size:10px}
.nav-about{margin-left:16px;width:30px}
.nav-services{margin-left:60px;width:40px}
.nav-gallery{margin-left:58px;width:40px}
.nav-blog{margin-left:57px;width:26px}
.nav-contact{margin-left:57px;width:42px}
.page-title{position:absolute;left:187px;top:122px;font-size:24px;font-weight:400;color:var(--navy)}
.hero{position:absolute;left:187px;top:162px;width:825px;height:292px;background:linear-gradient(150deg,#cdb8a0 0%,#c7c0b6 30%,#3f7ea0 55%,#1d4f6e 100%)}
.hero-arrow{position:absolute;top:132px;width:24px;height:26px;background:rgba(0,0,0,.8)}
.hero-arrow.prev{left:24px}.hero-arrow.next{right:24px}
.hero-arrow svg{display:block;margin:6px auto}
.hero-caption{position:absolute;left:0;bottom:0;width:100%;height:18px;background:rgba(0,0,0,.6);color:var(--white);font-size:9.5px;line-height:18px;padding-left:24px}
.intro{position:absolute;left:187px;top:476px;width:515px}
.intro h2{font-size:13px;font-weight:600;margin-bottom:3px}
.intro p{font-size:8px;line-height:16.5px;color:var(--body)}
.intro h2.sub{margin-top:14px;margin-bottom:6px}
.intro p + p{margin-top:8px}
.why{position:absolute;left:760px;top:477px;width:252px}
.why h3{font-size:13px;font-weight:600;color:var(--teal);margin-bottom:6px}
.why li{list-style:none;display:flex;align-items:center;gap:9px;font-size:12px;font-weight:300;color:#222;height:27.8px}
.projects-title{position:absolute;left:187px;top:751px;font-size:12px;font-weight:600}
.projects{position:absolute;left:187px;top:781px;display:flex;gap:30px}
.project{position:relative;width:184px;height:150px}
.p1{background:linear-gradient(180deg,#14306a 0%,#3b5d8e 55%,#6a8fb5 100%)}
.p2{background:linear-gradient(180deg,#2c2c2c,#4a4a46)}
.p3{background:linear-gradient(180deg,#8ea08a 0%,#a6b3a6 50%,#3f6e6e 100%)}
.p4{background:linear-gradient(160deg,#4d5a48 0%,#3aa6c8 55%,#a9d6e2 100%)}
.project-label{position:absolute;inset:0;display:flex;align-items:center;justify-content:center;text-align:center;color:var(--white);font-size:13px;font-weight:600;line-height:16px;background:rgba(0,0,0,.35)}
.scrubber{position:absolute;left:187px;top:946px;width:826px;height:12px}
.scrubber .track{position:absolute;left:12px;right:12px;top:5px;height:1px;background:#bbb}
.scrubber .thumb{position:absolute;left:22px;top:4px;width:233px;height:3px;background:#000}
.scrubber svg{position:absolute;top:0}
.site-footer{position:absolute;left:0;top:1038px;width:1200px;height:104px;background:var(--footer);color:var(--white)}
.footer-col{position:absolute;top:9px}
.footer-col h4{font-size:12.5px;font-weight:400;color:#e9e9e9;margin-bottom:5px;text-transform:uppercase}
.footer-col p{font-size:8.5px;font-weight:600;line-height:10.5px}
.footer-col p + p{margin-top:11px}
.col-contact{left:187px}.col-info{left:473px}.col-social{left:758px}
.social{display:flex;gap:22px;margin-top:9px}
.social a{display:flex;align-items:center;gap:5px;color:var(--white);text-decoration:none;font-size:10px;font-weight:600}
.social span.dot{width:14px;height:14px;background:#111}
.base-bar{position:absolute;left:0;top:1142px;width:1200px;height:30px;background:var(--footer-base);color:#ddd;font-size:8.5px;font-weight:600;line-height:30px;padding-left:187px}
</style>
</head>
<body>
<div class="page">
  <div class="top-strip"></div>
  <header class="site-header">
    <div class="brand"><span class="brand-mark"></span><span class="brand-name">Giles Fenton Pools</span></div>
    <nav class="main-nav">
      <a class="current" href="#">Home</a>
      <a class="nav-about" href="#">About</a>
      <a class="nav-services" href="#">Services</a>
      <a class="nav-gallery" href="#">Gallery</a>
      <a class="nav-blog" href="#">Blog</a>
      <a class="nav-contact" href="#">Contact</a>
    </nav>
  </header>

  <h1 class="page-title">Welcome to Giles Fenton Pools</h1>

  <section class="hero" role="img" aria-label="Slideshow photo of a curved fountain pool with spa and round fire pit on a stone deck">
    <span class="hero-arrow prev"><svg width="10" height="14" viewBox="0 0 10 14"><path d="M10 0L0 7l10 7z" fill="#fff"/></svg></span>
    <span class="hero-arrow next"><svg width="10" height="14" viewBox="0 0 10 14"><path d="M0 0l10 7-10 7z" fill="#fff"/></svg></span>
    <div class="hero-caption">Lorem ipsum - Fountain Pool</div>
  </section>

  <section class="intro">
    <h2>What we do?</h2>
    <p>We are a pool contracting company offering &nbsp;lorem ipsum. We are a pool contracting company offering &nbsp;lorem ipsum. We are a pool contracting company offering &nbsp;lorem ipsum. We are a pool contracting company offering &nbsp;lorem ipsum We are a pool contracting company offering &nbsp;lorem ipsum. We are a pool contracting company offering &nbsp;lorem ipsum.</p>
    <h2 class="sub">Some other main page subtitle.</h2>
    <p>That's just some of the services we offer at Giles Fenton Pool Contracting, Inc. you'll find quality, selection, and innovative planning and construction no matter what your pool needs may be. Some of our clients are developers including Marlow Homes, Q.R.T. Communities, Brennick Development, Halden Homes and Tessaro Homes ... but the customer is you during the design and construction of your new pool addition. As a commercially licensed contractor, Giles Fenton Pool Contracting, Inc. has completed pool design and installation for popular pool spots such as the Westmoor, Palmcrest Inn, Cedar Lakes Community Pool and Harbor Lakes, just to name a few.</p>
    <p>Because Giles Fenton Pool Contracting, Inc. is committed to bringing our customers only the best products, we are proud to offer Summit pools, part of the Garden Retreat concept of pools. These beautiful, high-quality pools are backed by a full warranty that ensures many years of enjoyment and recreation for your family.</p>
  </section>

  <aside class="why">
    <h3>Why choose us ?</h3>
    <ul>
      <li><svg width="10" height="13" viewBox="0 0 10 13"><path d="M0 0h4l6 6.5L4 13H0l6-6.5z" fill="var(--navy)"/></svg>Free Estimates</li>
      <li><svg width="10" height="13" viewBox="0 0 10 13"><path d="M0 0h4l6 6.5L4 13H0l6-6.5z" fill="var(--navy)"/></svg>Family Owned since 1979</li>
      <li><svg width="10" height="13" viewBox="0 0 10 13"><path d="M0 0h4l6 6.5L4 13H0l6-6.5z" fill="var(--navy)"/></svg>National Pool and Spa Guild Member</li>
      <li><svg width="10" height="13" viewBox="0 0 10 13"><path d="M0 0h4l6 6.5L4 13H0l6-6.5z" fill="var(--navy)"/></svg>Awarded over 75 NPSG Awards</li>
      <li><svg width="10" height="13" viewBox="0 0 10 13"><path d="M0 0h4l6 6.5L4 13H0l6-6.5z" fill="var(--navy)"/></svg>Free Design Consults Available</li>
    </ul>
  </aside>

  <h2 class="projects-title">Past Projects</h2>
  <div class="projects">
    <div class="project p1" role="img" aria-label="Lit two-storey villa with pool and palm trees at dusk"></div>
    <div class="project p2" role="img" aria-label="Night view of a pool with fire feature"><span class="project-label">Project Pompano Beach<br>Florida USA<br>2013</span></div>
    <div class="project p3" role="img" aria-label="Tiled spa with waterfall spilling into a pool"></div>
    <div class="project p4" role="img" aria-label="Aerial view of a freeform pool with spa among palms"></div>
  </div>
  <div class="scrubber">
    <svg style="left:0" width="10" height="12" viewBox="0 0 10 12"><path d="M9 6H1M5 2L1 6l4 4" stroke="#333" fill="none" stroke-width="1.2"/></svg>
    <span class="track"></span><span class="thumb"></span>
    <svg style="right:0" width="10" height="12" viewBox="0 0 10 12"><path d="M1 6h8M5 2l4 4-4 4" stroke="#333" fill="none" stroke-width="1.2"/></svg>
  </div>

  <footer class="site-footer">
    <div class="footer-col col-contact">
      <h4>Contact us</h4>
      <p>4410 NW 18 Lane<br>Coral Vista, Florida 33990</p>
      <p>&nbsp;555-010-4827</p>
      <p>contact@gilesfentonpools.example</p>
    </div>
    <div class="footer-col col-info">
      <h4>Other infos</h4>
      <p>Lorem ipsum</p>
      <p>Lorem ipsum<br>Lorem ipsumLorem ipsumLorem<br>ipsumLorem ipsumLorem ipsumLorem<br>ipsum</p>
    </div>
    <div class="footer-col col-social">
      <h4>Connect with us</h4>
      <div class="social">
        <a href="#"><span class="dot"></span>Videos</a>
        <a href="#"><span class="dot"></span>Friends</a>
        <a href="#"><span class="dot"></span>Boards</a>
        <a href="#"><span class="dot"></span>Circles</a>
      </div>
    </div>
  </footer>
  <div class="base-bar">© Giles Fenton Pools 2014. All Rights Reserved.</div>
</div>
</body>
</html>
```